Wedding Thank You post card

We would like to design a thank you post card for our wedding guests.
We want it to be a classic style with our photo and a simple 'Thank you' written and then Tom and Sylvia 15.03.2014' Where the writing does not obstruct our image.
We need 140 post cards
Sorry for the delay please find some photos you can use for the design process. One or all photos can be used. Thank you
Wedding

```html
<!DOCTYPE html>
<html lang="en">
<head>
<meta charset="utf-8">
<title>Tom and Sylvia – Wedding Thank You Postcard</title>
<link rel="stylesheet" href="https://fonts.googleapis.com/css2?family=Lobster&family=Federo&display=swap">
<style>
  :root {
    --backdrop: #000000;
    --card-green: #c8df84;
    --card-green-deep: #b5cd70;
    --ink-red: #c8424f;
    --ornament: #9fb868;
    --dot: #3e3e2e;
    --white: #ffffff;
    --photo-warm: #a7825f;
    --photo-dark: #4b3d33;
    --photo-soft: #d8c7b4;
  }
  * { box-sizing: border-box; margin: 0; padding: 0; }
  html, body { width: 784px; height: 1200px; overflow: hidden; background: var(--backdrop); }
  .canvas { position: relative; width: 784px; height: 1200px; }

  .card { position: absolute; left: 25px; width: 730px; background: var(--card-green); overflow: hidden; }
  .card--front { top: 29px; height: 563px; }
  .card--back { top: 611px; height: 562px; }

  .ornament { position: absolute; background: radial-gradient(ellipse, var(--card-green-deep), transparent 70%); opacity: .8; }

  .front-title {
    position: absolute; left: 34px; top: 104px;
    font-family: "Lobster", cursive; font-size: 46px; letter-spacing: 3px;
    color: var(--ink-red);
  }
  .photo-strip { position: absolute; left: 0; top: 187px; width: 730px; height: 244px; background: var(--white); }
  .photo { position: absolute; }
  .photo--warm { background: linear-gradient(160deg, var(--photo-soft), var(--photo-warm)); }
  .photo--dark { background: linear-gradient(160deg, var(--photo-warm), var(--photo-dark)); }

  .couple-names {
    font-family: "Federo", sans-serif; color: var(--ink-red); text-transform: uppercase;
    border-bottom: 2px solid var(--ink-red); display: inline-block; line-height: 1.1;
  }
  .front-caption { position: absolute; left: 0; width: 730px; top: 443px; text-align: center; }
  .front-caption .couple-names { font-size: 35px; letter-spacing: 1px; padding: 0 4px 2px; }
  .front-caption .date { display: inline-block; margin-top: 12px; font-size: 33px; }

  .back-scene { position: absolute; inset: 0; background: linear-gradient(100deg, var(--card-green-deep) 0%, var(--card-green) 45%, var(--card-green-deep) 100%); opacity: .9; }
  .dotted-frame { position: absolute; left: 22px; top: 18px; width: 692px; height: 524px; border: 3px dotted var(--dot); }
  .stamp-box { position: absolute; left: 550px; top: 17px; width: 161px; height: 163px; background: var(--white); }
  .back-heading { position: absolute; left: 58px; top: 98px; }
  .back-heading .couple-names { font-size: 27px; letter-spacing: 1px; padding-right: 6px; }
  .back-heading .date { display: inline-block; margin: 14px 0 0 68px; font-size: 26px; }
  .message {
    position: absolute; left: 51px; top: 202px; width: 280px;
    font-family: "Federo", sans-serif; text-transform: uppercase; color: var(--ink-red);
    font-size: 17px; line-height: 36px; letter-spacing: .5px;
  }
  .divider { position: absolute; left: 346px; top: 182px; height: 280px; border-left: 3px dotted var(--dot); }
  .address-line { position: absolute; left: 375px; width: 313px; height: 2px; background: var(--white); }
</style>
</head>
<body>
<div class="canvas">

  <section class="card card--front">
    <div class="ornament" role="img" aria-label="Paisley line ornament" style="left:390px;top:-20px;width:350px;height:170px;"></div>
    <div class="ornament" role="img" aria-label="Floral line ornament" style="left:0;top:440px;width:360px;height:130px;"></div>
    <div class="ornament" role="img" aria-label="Floral line ornament" style="left:530px;top:440px;width:210px;height:130px;"></div>

    <h1 class="front-title">THANK YOU....</h1>

    <div class="photo-strip">
      <div class="photo photo--warm" role="img" aria-label="Wedding photo: couple seated on red steps" style="left:19px;top:7px;width:130px;height:111px;"></div>
      <div class="photo photo--warm" role="img" aria-label="Wedding photo: bride and groom smiling with bouquet" style="left:155px;top:7px;width:85px;height:232px;"></div>
      <div class="photo photo--dark" role="img" aria-label="Wedding photo: couple toasting" style="left:248px;top:7px;width:129px;height:111px;"></div>
      <div class="photo photo--warm" role="img" aria-label="Wedding photo: couple lying on red carpet" style="left:19px;top:124px;width:130px;height:115px;"></div>
      <div class="photo photo--warm" role="img" aria-label="Wedding photo: couple kissing" style="left:248px;top:124px;width:129px;height:115px;"></div>
      <div class="photo photo--dark" role="img" aria-label="Wedding photo: couple kissing in front of guests" style="left:396px;top:7px;width:316px;height:232px;"></div>
    </div>

    <div class="front-caption">
      <span class="couple-names">Tom and Sylvia</span><br>
      <span class="couple-names date">15.03.2014</span>
    </div>
  </section>

  <section class="card card--back">
    <div class="back-scene" role="img" aria-label="Faded photo of the wedding venue"></div>
    <div class="dotted-frame"></div>
    <div class="stamp-box"></div>

    <div class="back-heading">
      <span class="couple-names">Tom and Sylvia</span><br>
      <span class="couple-names date">15.03.2014</span>
    </div>

    <p class="message">Thank God that we have friends like you! Your kindness and presence, your big and open hearts made our wedding day never-to-be-forgotten. Thanks a lot.</p>

    <div class="divider"></div>
    <div class="address-line" style="top:244px;"></div>
    <div class="address-line" style="top:289px;"></div>
    <div class="address-line" style="top:333px;"></div>
    <div class="address-line" style="top:377px;"></div>
    <div class="address-line" style="top:420px;"></div>
  </section>

</div>
</body>
</html>
```